Business Card design for shipping company 'FERNHOLT INTERNATIONAL LTD'

Classic / traditional business card in black Garamond / Times New Roman or similar text for a shipping / marine transport company, containing the following information:

QUOTE

FERNHOLT INTERNATIONAL LTD

MARTIN QUESTEDGE FICS

T: +44 7902 615370
E: cargo@fernholt-example.com

UNQUOTE

Target Market(s)

Marine / Shipping industry

Contact Information for Business Card

FERNHOLT INTERNATIONAL LTD MARTIN QUESTEDGE FICS T: +44 7902 615370 E: cargo@fernholt-example.com

Font styles to use
Serif

Colors

Designer to choose colors to be used in the design.

Requirements
Must have
• Garamond / Times New Roman or similar text in black colour

```html
<!DOCTYPE html>
<html lang="en">
<head>
<meta charset="utf-8">
<title>Fernholt International Ltd — Business Card</title>
<link rel="stylesheet" href="https://fonts.googleapis.com/css2?family=EB+Garamond:wght@400;500;600;700&display=swap">
<style>
  :root {
    --backdrop: #3b3b3b;
    --card-black: #000000;
    --card-white: #ffffff;
    --ink: #111111;
    --paper-text: #ffffff;
    --rule: #222222;
  }
  * { margin: 0; padding: 0; box-sizing: border-box; }
  html, body {
    width: 1200px;
    height: 998px;
    overflow: hidden;
    background: var(--backdrop);
    font-family: "EB Garamond", "Times New Roman", serif;
  }
  .canvas {
    width: 1200px;
    height: 998px;
    display: flex;
    flex-direction: column;
    align-items: center;
    justify-content: center;
    gap: 64px;
  }
  .card {
    width: 640px;
    height: 366px;
    position: relative;
    box-shadow: 0 10px 28px rgba(0,0,0,0.45);
  }
  .card--front {
    background: var(--card-black);
    color: var(--paper-text);
    display: flex;
    align-items: center;
    justify-content: center;
    text-align: center;
  }
  .front-name {
    font-weight: 600;
    font-size: 46px;
    line-height: 1.08;
    letter-spacing: 1px;
  }
  .card--back {
    background: var(--card-white);
    color: var(--ink);
    text-align: center;
  }
  .quote-mark {
    position: absolute;
    top: 52px;
    left: 0; right: 0;
    font-weight: 600;
    font-size: 22px;
    letter-spacing: 1px;
  }
  .company-band {
    position: absolute;
    top: 96px;
    left: 0; right: 0;
    height: 48px;
    background: var(--card-black);
    color: var(--paper-text);
    font-weight: 600;
    font-size: 28px;
    line-height: 48px;
    letter-spacing: 0.5px;
  }
  .person-name {
    position: absolute;
    top: 170px;
    left: 0; right: 0;
    font-weight: 600;
    font-size: 30px;
    letter-spacing: 0.5px;
  }
  .divider {
    position: absolute;
    top: 218px;
    left: 150px;
    right: 150px;
    display: flex;
    align-items: center;
    gap: 6px;
  }
  .divider-rule {
    flex: 1;
    height: 1px;
    background: var(--rule);
  }
  .divider svg { display: block; }
  .contact {
    position: absolute;
    top: 246px;
    left: 0; right: 0;
    font-size: 17px;
    line-height: 27px;
  }
  .unquote-mark {
    position: absolute;
    top: 306px;
    left: 0; right: 0;
    font-weight: 400;
    font-size: 24px;
    letter-spacing: 1px;
  }
</style>
</head>
<body>
  <main class="canvas">
    <section class="card card--front">
      <h1 class="front-name">FERNHOLT<br>INTERNATIONAL LTD</h1>
    </section>

    <section class="card card--back">
      <p class="quote-mark">QUOTE</p>
      <div class="company-band">FERNHOLT INTERNATIONAL LTD</div>
      <p class="person-name">MARTIN QUESTEDGE FICS</p>
      <div class="divider">
        <span class="divider-rule"></span>
        <svg width="20" height="20" viewBox="0 0 20 20" aria-label="Phone">
          <circle cx="10" cy="10" r="9.5" fill="#111"/>
          <path d="M6.5 5.5 L8.3 5.2 L9.2 7.6 L8 8.5 Q9 10.9 11.5 12 L12.4 10.8 L14.8 11.7 L14.5 13.5 Q13.8 14.6 12 14.3 Q7 12.8 5.7 8 Q5.4 6.2 6.5 5.5 Z" fill="#fff"/>
        </svg>
        <svg width="20" height="20" viewBox="0 0 20 20" aria-label="Email">
          <circle cx="10" cy="10" r="9.5" fill="#111"/>
          <rect x="5" y="6.5" width="10" height="7" fill="none" stroke="#fff" stroke-width="1.2"/>
          <path d="M5 6.5 L10 10.8 L15 6.5" fill="none" stroke="#fff" stroke-width="1.2"/>
        </svg>
        <span class="divider-rule"></span>
      </div>
      <p class="contact">
        +44 7902 615370<br>
        cargo@fernholt-example.com
      </p>
      <p class="unquote-mark">UNQUOTE</p>
    </section>
  </main>
</body>
</html>
```